Brightmoor Hotel Management Consulting Solutions needs website design.

I need a clear simple website design for a new company in Western Australia providing Hotel Management expertise through consulting services / solutions / advice. I have a logo and need a website designed. I would like the logo to be the hero of the website. I would like modern, cutting edge design to reflect the professional service I will be supplying. See logo attached to assist (in website files). The purpose of the website is to inform basic business information linking to my email addresses, including Facebook and Instagram. I want to show that my services can benefit all private and commercial hotel / resort / type businesses using my vast 25 years international Hotel experience from 3 star to 5 star hotels and resorts with a respected hotel group, to grow their business or trouble shooting. Key Services, through a menu bar to include, Hotel Keystone Operations, Hotel Budgeting / Business Plans, Business Strategies, Revenue Management, Financial advice, Cost Management Solutions, Pre-Opening Hotel Overview, Hotel Marketing, Investor Communications Support, Asset Management, Hotel Real Estate Investment advice, People Management. I want the menu bar titles to include About me, showing my experience, Hotel Keystone Services (to then drop down to all the above hotel services, then drop down to a brief description of each hotel department), Contact details, etc.

```html
<!DOCTYPE html>
<html lang="en">
<head>
<meta charset="utf-8">
<title>Brightmoor Hotel Management Consulting Solutions</title>
<link href="https://fonts.googleapis.com/css2?family=Fira+Sans:wght@400;500;600&family=Montserrat:wght@700;800&family=Poppins:wght@300;400;500&display=swap" rel="stylesheet">
<style>
:root{
  --navy:#1b2235;
  --navy-2:#242d45;
  --ink:#1f2433;
  --text:#3b4050;
  --muted:#7d8190;
  --white:#ffffff;
  --pale:#eef3fd;
  --card:#f4f4f5;
  --line:#c9ccd3;
}
*{box-sizing:border-box;margin:0;padding:0}
html,body{width:1200px;height:5102px;overflow:hidden}
body{position:relative;background:var(--white);font-family:"Poppins",sans-serif;color:var(--text)}
.abs{position:absolute}
h2,h3,h4{font-family:"Fira Sans",sans-serif;color:var(--ink);font-weight:600}

/* header */
.site-header{left:0;top:0;width:1200px;height:150px;background:var(--white);z-index:3}
.brand-badge{left:155px;top:-40px;width:250px;height:260px;border-radius:0 0 125px 125px;background:var(--white);z-index:4;display:flex;flex-direction:column;align-items:center;justify-content:flex-end;padding-bottom:52px}
.brand-badge .mark{width:64px;height:64px;border-radius:50%;border:4px solid var(--navy);margin-bottom:14px}
.brand-badge .name{font:700 10.5px/1.3 "Montserrat",sans-serif;color:var(--navy);text-align:center;text-transform:uppercase}
.contact-mail{left:648px;top:26px;display:flex;align-items:center;gap:10px;z-index:4}
.contact-mail .ic{width:36px;height:36px;border-radius:50%;background:var(--navy);display:flex;align-items:center;justify-content:center}
.contact-mail small{display:block;font:500 13px "Poppins",sans-serif;color:var(--ink)}
.contact-mail span{font:400 17px "Poppins",sans-serif;color:var(--ink)}
.social{left:948px;top:32px;display:flex;gap:8px;z-index:4}
.social i{width:36px;height:36px;border-radius:50%;background:var(--navy);display:block}
.main-nav{left:607px;top:100px;display:flex;gap:31px;z-index:4}
.main-nav a{font:500 14px "Poppins",sans-serif;color:var(--ink);text-decoration:none;text-transform:uppercase}

/* hero */
.hero{left:0;top:150px;width:1200px;height:670px;background:linear-gradient(180deg,#a9bfd6 0%,#d5dde6 38%,#7f93a3 55%,#4e5a5f 78%,#5c5752 100%)}
.hero-title{left:0;top:372px;width:1200px;text-align:center;font:800 36px/1.3 "Montserrat",sans-serif;letter-spacing:1.5px;color:var(--navy);text-transform:uppercase}
.feature{width:270px;height:270px;border-radius:50%;background:var(--white);box-shadow:0 6px 18px rgba(0,0,0,.18);border:2px solid var(--navy);text-align:center;padding-top:150px}
.feature .top{position:absolute;left:50%;top:-8px;transform:translateX(-50%);width:150px;height:120px;border-radius:0 0 75px 75px;background:var(--navy);display:flex;align-items:center;justify-content:center}
.feature h3{font:500 18px "Fira Sans",sans-serif;color:var(--ink);text-transform:uppercase;margin-bottom:10px}
.feature p{font:400 12px/1.6 "Poppins",sans-serif;color:var(--text);padding:0 50px}
.feature.dark{width:292px;height:292px;background:var(--navy);border-color:var(--white);padding-top:158px}
.feature.dark .top{background:var(--white);width:130px;height:130px;border-radius:50%;top:14px}
.feature.dark h3,.feature.dark p{color:var(--white)}

/* intro */
.intro h2{left:0;top:1068px;width:1200px;text-align:center;font-size:26px;text-transform:uppercase}
.intro p{left:170px;top:1128px;width:860px;text-align:center;font:400 12px/2.1 "Poppins",sans-serif}
.photo-card{width:272px;height:355px;color:var(--white);text-align:center;display:flex;flex-direction:column;justify-content:flex-end;padding:0 12px 22px}
.photo-card h3{font:600 17px "Fira Sans",sans-serif;color:var(--white);text-transform:uppercase;margin-bottom:8px;white-space:nowrap}
.photo-card p{font:400 13px/1.6 "Poppins",sans-serif;padding:0 8px}

/* about */
.about{left:0;top:1752px;width:1200px;height:520px;background:linear-gradient(100deg,#1c2438,#2a3450 45%,#1b2235)}
.about .art{left:165px;top:80px;width:430px;height:360px;border-radius:8px;background:radial-gradient(circle at 45% 45%,#5a6477,#2b3449 70%)}
.about h2{left:652px;top:84px;color:var(--white);font-size:26px}
.about p{left:652px;top:142px;width:378px;font:400 13px/1.95 "Fira Sans",sans-serif;color:#dfe3ec;text-align:justify}
.btn-light{left:652px;top:395px;width:110px;height:50px;background:var(--white);color:var(--ink);font:500 12px/50px "Poppins",sans-serif;text-align:center;text-transform:uppercase}

/* services list */
.services-band{left:0;top:2272px;width:645px;height:690px;background:var(--pale)}
.services-dots{left:608px;top:2316px;width:160px;height:120px;background-image:radial-gradient(#c3c9d6 1.2px,transparent 1.3px);background-size:8px 8px}
.services-photo{left:645px;top:2350px;width:555px;height:675px;background:linear-gradient(90deg,#3a2a1c,#8a6a45 35%,#d9c6a6 55%,#6b4f33 80%,#2d2117)}
.services-title{left:172px;top:2370px;font-size:26px;text-transform:uppercase}
.svc-item{left:172px;display:flex;align-items:center;gap:22px}
.svc-item .ic{width:86px;height:86px;border-radius:50%;background:var(--navy);border:4px solid #d9deea;display:flex;align-items:center;justify-content:center}
.svc-item h4{font:500 18px "Fira Sans",sans-serif;text-transform:uppercase;margin-bottom:6px}
.svc-item p{font:400 13px "Poppins",sans-serif}

/* service grid */
.grid-title{left:0;top:3100px;width:1200px;text-align:center;font-size:26px;text-transform:uppercase}
.svc-card{width:210px;height:298px;background:var(--card);text-align:center;padding-top:26px}
.svc-card .ic{height:64px;display:flex;align-items:center;justify-content:center}
.svc-card h4{font:500 12.5px/1.4 "Fira Sans",sans-serif;text-transform:uppercase;margin:14px 16px 14px;min-height:36px}
.svc-card p{font:400 11px/1.65 "Poppins",sans-serif;color:var(--muted);padding:0 30px}
.svc-card .more{display:inline-block;margin-top:18px;border:1px solid var(--ink);font:500 8px/16px "Poppins",sans-serif;padding:0 7px;text-transform:uppercase;color:var(--ink)}
.svc-card.active{background:linear-gradient(160deg,#2a3452,#1b2235)}
.svc-card.active h4,.svc-card.active p{color:var(--white)}
.svc-card.active .more{border-color:var(--white);color:var(--white)}

/* why */
.why{left:0;top:3872px;width:1200px;height:748px;background:linear-gradient(180deg,#232b40,#1b2235)}
.why h2{left:0;top:138px;width:1200px;text-align:center;color:var(--white);font-size:26px;text-transform:uppercase}
.why-emblem{left:460px;top:218px;width:280px;height:250px;border-radius:12px;background:radial-gradient(circle at 50% 45%,#3a4560,#232b40 75%)}
.why-point h4{font:500 14px "Fira Sans",sans-serif;color:var(--white);text-transform:uppercase;margin-bottom:8px;white-space:nowrap}
.why-point p{font:400 12px/1.9 "Poppins",sans-serif;color:#dfe3ec}
.why .node{width:78px;height:78px;border-radius:50%;background:var(--white);display:flex;align-items:center;justify-content:center}

/* contact */
.contact{left:0;top:4620px;width:1200px;height:482px;background:var(--pale)}
.contact h2{left:172px;top:70px;font-size:26px;text-transform:uppercase}
.ct-ic{width:72px;height:72px;border-radius:50%;border:2px solid var(--ink);display:flex;align-items:center;justify-content:center}
.ct-block h4{font:500 17px "Fira Sans",sans-serif;text-transform:uppercase;margin-bottom:8px}
.ct-block p{font:400 12px/2 "Poppins",sans-serif;color:var(--ink)}
.contact-brand{left:690px;top:140px;width:350px;text-align:center}
.contact-brand .mark{width:110px;height:110px;border-radius:50%;border:6px solid var(--navy);margin:0 auto 20px}
.contact-brand .name{font:700 15px/1.4 "Montserrat",sans-serif;color:var(--navy);text-transform:uppercase}
.rule{left:172px;top:400px;width:856px;height:1px;background:var(--line)}
.copyright{left:0;top:436px;width:1200px;text-align:center;font:400 12px "Poppins",sans-serif;color:var(--ink)}
</style>
</head>
<body>

<header class="abs site-header">
  <div class="abs brand-badge"><div class="mark"></div><div class="name">Brightmoor Hotel Management<br>Consulting - Solutions</div></div>
  <div class="abs contact-mail">
    <div class="ic"><svg width="18" height="14" viewBox="0 0 18 14"><rect x="1" y="1" width="16" height="12" fill="none" stroke="#fff" stroke-width="1.6"/><path d="M1 1l8 7 8-7" fill="none" stroke="#fff" stroke-width="1.6"/></svg></div>
    <div><small>Email:</small><span>info@brightmoorhm.com</span></div>
  </div>
  <div class="abs social" aria-label="Social links"><i></i><i></i></div>
  <nav class="abs main-nav"><a>Home</a><a>About Me</a><a>Hotel Keystone Services</a><a>Contact</a></nav>
</header>

<section class="abs hero" role="img" aria-label="Photo of a modern beachfront resort with infinity pool and sea view"></section>
<h1 class="abs hero-title">Brightmoor Hotel Management<br>Consulting - Solutions</h1>

<div class="abs feature" style="left:175px;top:655px">
  <div class="top"><svg width="46" height="54" viewBox="0 0 46 54" fill="none" stroke="#fff" stroke-width="2"><rect x="6" y="4" width="22" height="46"/><rect x="28" y="20" width="14" height="30"/><path d="M11 10h4M19 10h4M11 18h4M19 18h4M11 26h4M19 26h4M11 34h4M19 34h4M33 28h4M33 36h4M2 50h42"/></svg></div>
  <h3>Private Hotel</h3><p>Duis aute irure dolor in reprehenderit in voluptate velit esse</p>
</div>
<div class="abs feature dark" style="left:454px;top:674px">
  <div class="top"><svg width="46" height="56" viewBox="0 0 46 56"><path d="M23 2C11 2 3 11 3 22c0 15 20 32 20 32s20-17 20-32C43 11 35 2 23 2z" fill="#1b2235"/><rect x="12" y="18" width="22" height="10" rx="2" fill="#fff"/><rect x="12" y="14" width="6" height="5" fill="#fff"/></svg></div>
  <h3>Resort</h3><p>Duis aute irure dolor in reprehenderit in voluptate velit esse</p>
</div>
<div class="abs feature" style="left:757px;top:655px">
  <div class="top"><svg width="60" height="56" viewBox="0 0 60 56" fill="none" stroke="#fff" stroke-width="2"><path d="M14 4h32"/><rect x="8" y="10" width="44" height="40"/><path d="M14 18h32M14 26h32M14 34h32M26 50v-8h8v8M2 50h56"/></svg></div>
  <h3>Commercial Hotel</h3><p>Duis aute irure dolor in reprehenderit in voluptate velit esse</p>
</div>

<section class="intro">
  <h2 class="abs">Brightmoor Hotel Management Consulting</h2>
  <p class="abs">Nemo enim ipsam voluptatem quia voluptas sit aspernatur aut odit aut fugit, sed quia consequuntur magni dolores eos qui ratione voluptatem sequi nesciunt. Neque porro quisquam est, qui dolorem ipsum quia dolor sit amet, consectetur, adipisci velit, sed quia non numquam eius modi tempora incidunt ut labore et dolore magnam aliquam quaerat voluptatem.</p>
</section>

<div class="abs photo-card" style="left:28px;top:1305px;background:linear-gradient(180deg,#3d6fae 0%,#7fa3c8 40%,#6a5a4c 70%,#1e2230 100%)" role="img" aria-label="Photo of beach cabanas at sunset">
  <h3>Hotel Keystone Operations</h3><p>Duis aute irure dolor in reprehen derit in voluptate</p></div>
<div class="abs photo-card" style="left:318px;top:1275px;background:linear-gradient(180deg,#8f8aa8 0%,#c6b3b8 35%,#5e6b80 65%,#1c2030 100%)" role="img" aria-label="Photo of a seaside lounge bed under a cloudy sky">
  <h3>Hotel Budgeting</h3><p>Duis aute irure dolor in reprehen derit in voluptate</p></div>
<div class="abs photo-card" style="left:608px;top:1305px;background:linear-gradient(180deg,#5d90c4 0%,#3d7a5c 40%,#2c8fa0 70%,#1c2231 100%)" role="img" aria-label="Photo of a palm-lined resort pool">
  <h3>Business Plans</h3><p>Duis aute irure dolor in reprehen derit in voluptate</p></div>
<div class="abs photo-card" style="left:898px;top:1275px;background:linear-gradient(180deg,#9fb8c8 0%,#c8b89a 40%,#6e6a58 70%,#1c2030 100%)" role="img" aria-label="Photo of sun loungers by a pool with palm trees">
  <h3>People Management</h3><p>Duis aute irure dolor in reprehen derit in voluptate</p></div>

<section class="abs about">
  <div class="abs art" role="img" aria-label="Faint photo of business people behind a large brand emblem"></div>
  <h2 class="abs">About Me</h2>
  <p class="abs">At vero eos et accusamus et iusto odio dignissimos ducimus qui blanditiis praesentium voluptatum deleniti atque corrupti quos dolores et quas molestias excepturi sint occaecati cupiditate non provident, similique sunt in culpa qui officia deserunt mollitia animi, id est laborum et dolorum fuga. Et harum quidem rerum facilis est et expedita distinctio. Nam libero tempore, cum soluta nobis est eligendi optio cumque nihil impedit quo minus id quod maxime placeat.</p>
  <div class="abs btn-light">Read More</div>
</section>

<div class="abs services-band"></div>
<div class="abs services-dots"></div>
<div class="abs services-photo" role="img" aria-label="Photo of a luxury hotel lobby with marble floor and chandelier"></div>
<h2 class="abs services-title">Our Hotel Services</h2>
<div class="abs svc-item" style="top:2453px"><div class="ic"><svg width="34" height="34" viewBox="0 0 34 34" fill="none" stroke="#fff" stroke-width="2"><rect x="4" y="4" width="20" height="26"/><path d="M9 12h10M9 18h10M9 24h6"/><circle cx="26" cy="24" r="6"/></svg></div><div><h4>Revenue Management</h4><p>Nemo enim ipsam voluptatem quia voluptas</p></div></div>
<div class="abs svc-item" style="top:2558px"><div class="ic"><svg width="34" height="34" viewBox="0 0 34 34" fill="none" stroke="#fff" stroke-width="2"><circle cx="17" cy="10" r="6"/><path d="M6 32c0-8 5-13 11-13s11 5 11 13"/></svg></div><div><h4>Financial Advice</h4><p>Nemo enim ipsam voluptatem quia voluptas</p></div></div>
<div class="abs svc-item" style="top:2663px"><div class="ic"><svg width="34" height="34" viewBox="0 0 34 34" fill="none" stroke="#fff" stroke-width="2"><circle cx="17" cy="11" r="6"/><path d="M7 30c0-7 4-11 10-11s10 4 10 11M4 30h26"/></svg></div><div><h4>Cost Management Solutions</h4><p>Nemo enim ipsam voluptatem quia voluptas</p></div></div>
<div class="abs svc-item" style="top:2768px"><div class="ic"><svg width="34" height="34" viewBox="0 0 34 34" fill="none" stroke="#fff" stroke-width="2"><rect x="4" y="8" width="26" height="22"/><path d="M4 14h26M10 4v8M24 4v8M10 20h4M18 20h4M10 25h4"/></svg></div><div><h4>Pre-Opening Hotel Overview</h4><p>Nemo enim ipsam voluptatem quia voluptas</p></div></div>

<h2 class="abs grid-title">Hotel Keystone Services</h2>
<svg width="0" height="0" style="position:absolute"><defs>
  <g id="ic-doc" fill="none" stroke="#1b2235" stroke-width="2"><rect x="14" y="6" width="28" height="40"/><path d="M20 16h16M20 24h16M20 32h10"/></g>
  <g id="ic-chart" fill="none" stroke="#1b2235" stroke-width="2"><path d="M8 48h40M14 46V30M24 46V22M34 46V14M44 46V8"/></g>
  <g id="ic-bubble" fill="none" stroke="#1b2235" stroke-width="2"><rect x="8" y="10" width="40" height="26" rx="4"/><path d="M18 36l-4 10 12-10M16 20h24M16 27h16"/></g>
</defs></svg>
<div class="abs svc-card" style="left:162px;top:3180px"><div class="ic"><svg width="56" height="56"><rect x="12" y="12" width="32" height="32" rx="4" fill="none" stroke="#1b2235" stroke-width="2"/><path d="M20 28l6 6 10-12" fill="none" stroke="#1b2235" stroke-width="2"/></svg></div><h4>Hotel Keystone<br>Operations</h4><p>Lorem ipsum is simply dummy text of the printing and type setting industry Lorem ip</p><span class="more">Read More</span></div>
<div class="abs svc-card active" style="left:384px;top:3180px"><div class="ic"><svg width="56" height="56" viewBox="0 0 56 56"><rect x="14" y="6" width="28" height="40" fill="none" stroke="#fff" stroke-width="2"/><path d="M20 16h16M20 24h16M20 32h10" stroke="#fff" stroke-width="2"/></svg></div><h4>Hotel Budgeting /<br>Business Plans</h4><p>Lorem ipsum is simply dummy text of the printing and type setting industry Lorem ip</p><span class="more">Read More</span></div>
<div class="abs svc-card" style="left:606px;top:3180px"><div class="ic"><svg width="56" height="56"><use href="#ic-chart"/></svg></div><h4>Business<br>Strategies</h4><p>Lorem ipsum is simply dummy text of the printing and type setting industry Lorem ip</p><span class="more">Read More</span></div>
<div class="abs svc-card" style="left:828px;top:3180px"><div class="ic"><svg width="56" height="56"><use href="#ic-chart"/></svg></div><h4>Revenue<br>Management</h4><p>Lorem ipsum is simply dummy text of the printing and type setting industry Lorem ip</p><span class="more">Read More</span></div>
<div class="abs svc-card" style="left:162px;top:3492px"><div class="ic"><svg width="56" height="56"><use href="#ic-doc"/></svg></div><h4>Financial<br>Advice</h4><p>Lorem ipsum is simply dummy text of the printing and type setting industry Lorem ip</p><span class="more">Read More</span></div>
<div class="abs svc-card" style="left:384px;top:3492px"><div class="ic"><svg width="56" height="56"><circle cx="28" cy="30" r="16" fill="none" stroke="#1b2235" stroke-width="2"/><path d="M28 4v10M12 10l6 6M44 10l-6 6" stroke="#1b2235" stroke-width="2"/></svg></div><h4>Cost Management<br>Solutions</h4><p>Lorem ipsum is simply dummy text of the printing and type setting industry Lorem ip</p><span class="more">Read More</span></div>
<div class="abs svc-card" style="left:606px;top:3492px"><div class="ic"><svg width="56" height="56"><path d="M8 22h10l20-12v36L18 34H8z" fill="none" stroke="#1b2235" stroke-width="2"/></svg></div><h4>Hotel<br>Marketing</h4><p>Lorem ipsum is simply dummy text of the printing and type setting industry Lorem ip</p><span class="more">Read More</span></div>
<div class="abs svc-card" style="left:828px;top:3492px"><div class="ic"><svg width="56" height="56"><use href="#ic-bubble"/></svg></div><h4>Investor<br>Communications Support</h4><p>Lorem ipsum is simply dummy text of the printing and type setting industry Lorem ip</p><span class="more">Read More</span></div>

<section class="abs why">
  <h2 class="abs">Why Chose Us</h2>
  <div class="abs why-emblem" role="img" aria-label="Large brand emblem linking the three service points"></div>
  <div class="abs node" style="left:368px;top:318px"><svg width="40" height="40"><circle cx="20" cy="14" r="7" fill="none" stroke="#1b2235" stroke-width="2"/><path d="M6 36c0-9 6-14 14-14s14 5 14 14" fill="none" stroke="#1b2235" stroke-width="2"/></svg></div>
  <div class="abs node" style="left:748px;top:318px"><svg width="40" height="40"><circle cx="20" cy="14" r="7" fill="none" stroke="#1b2235" stroke-width="2"/><path d="M6 36c0-9 6-14 14-14s14 5 14 14" fill="none" stroke="#1b2235" stroke-width="2"/></svg></div>
  <div class="abs node" style="left:561px;top:502px"><svg width="40" height="40"><rect x="6" y="8" width="28" height="24" fill="none" stroke="#1b2235" stroke-width="2"/><path d="M12 16h16M12 24h10" stroke="#1b2235" stroke-width="2"/></svg></div>
  <div class="abs why-point" style="left:130px;top:290px;width:222px;text-align:right"><h4>Hotel Keystone Operations</h4><p>Lorem ipsum dolor sit amet, consecte tur adipiscing elit, sed do eiusmod tempor incididunt</p></div>
  <div class="abs why-point" style="left:846px;top:290px;width:222px"><h4>Revenue Management</h4><p>Lorem ipsum dolor sit amet, consecte tur adipiscing elit, sed do eiusmod tempor incididunt</p></div>
  <div class="abs why-point" style="left:480px;top:596px;width:240px;text-align:center"><h4>Cost Controlling</h4><p>Lorem ipsum dolor sit amet, consecte tur adipiscing elit, sed do eiusmod tempor incididunt</p></div>
</section>

<section class="abs contact">
  <h2 class="abs">Contact Us</h2>
  <div class="abs ct-ic" style="left:172px;top:148px"><svg width="30" height="30" viewBox="0 0 30 30"><path d="M7 3l5 5-3 4c2 4 5 7 9 9l4-3 5 5-4 4C13 26 4 17 3 7z" fill="none" stroke="#1f2433" stroke-width="1.8"/></svg></div>
  <div class="abs ct-ic" style="left:418px;top:148px"><svg width="26" height="32" viewBox="0 0 26 32"><path d="M13 2C7 2 3 6.5 3 12c0 8 10 18 10 18s10-10 10-18C23 6.5 19 2 13 2z" fill="none" stroke="#1f2433" stroke-width="1.8"/><circle cx="13" cy="12" r="4" fill="none" stroke="#1f2433" stroke-width="1.8"/></svg></div>
  <div class="abs ct-block" style="left:172px;top:242px"><h4>Call Us</h4><p>+61 8 5550 2481<br>info@brightmoorhm.com</p></div>
  <div class="abs ct-block" style="left:418px;top:242px"><h4>Address</h4><p>#48, Harbourview Stop,<br>Marina Main Road,<br>Australia, 6160.</p></div>
  <div class="abs contact-brand"><div class="mark"></div><div class="name">Brightmoor Hotel Management<br>Consulting - Solutions</div></div>
  <div class="abs rule"></div>
  <p class="abs copyright">Copyrights @ 2021 Brightmoor Hotel Management Consulting. All Rights Reserved</p>
</section>

</body>
</html>
```